Varuko Business Card

I am looking for a business card design for a start-up company called Varuko Group. This is a management consultancy focused on sales, marketing, sales management, product management and AGILE software development. Our primary customers are $1M to $50M in revenue.

Varuko is the Italian word for "slope."

The path from $0 to $50M has many different growth stages associated with it. Each one having a significant slope to the next plateau. Our expertise helps our customers ascend each of those slopes. We bring experience, successful track-records in growing companies, best practices and a dive-in and roll-up your sleeves mentality. We are not sitting at base camp shouting instructions, we are right there with you, on the climb.

```html
<!DOCTYPE html>
<html lang="en">
<head>
<meta charset="utf-8">
<title>Varuko Business Card</title>
<link rel="stylesheet" href="https://fonts.googleapis.com/css2?family=Open+Sans:wght@400;600&family=Questrial&display=swap">
<style>
  :root {
    --backdrop: #2b2b2b;
    --card-white: #f4f4f4;
    --ink: #4f5a63;
    --ink-soft: #6b757d;
    --green: #5e9534;
    --green-pale: #b9d99a;
    --blue: #0b74b8;
    --white: #ffffff;
  }
  * { box-sizing: border-box; margin: 0; padding: 0; }
  html, body { width: 1200px; height: 900px; overflow: hidden; }
  body {
    background: var(--backdrop);
    font-family: "Open Sans", sans-serif;
    display: flex;
    align-items: center;
    justify-content: center;
    gap: 50px;
  }
  .card {
    width: 540px;
    height: 310px;
    border-radius: 22px;
    position: relative;
    overflow: hidden;
    box-shadow: 0 12px 30px rgba(0,0,0,.45);
  }

  /* back of card */
  .card-back { background: var(--green); }
  .card-back .side-band {
    position: absolute; left: 0; top: 0; bottom: 0;
    width: 150px; background: var(--blue);
    border-right: 24px solid var(--white);
  }
  .card-back .brand-name {
    position: absolute; right: 40px; bottom: 34px;
    font-family: "Questrial", sans-serif;
    font-size: 64px; line-height: 1; color: var(--white);
    letter-spacing: 1px;
    white-space: nowrap;
  }

  /* front of card */
  .card-front { background: var(--card-white); }
  .brand {
    position: absolute; left: 44px; top: 40px;
    display: flex; align-items: center; gap: 18px;
  }
  .brand-dot { width: 48px; height: 48px; border-radius: 50%; background: var(--green); }
  .brand-word {
    font-family: "Questrial", sans-serif;
    font-size: 58px; line-height: 1; color: var(--ink);
  }
  .person { position: absolute; left: 130px; top: 132px; color: var(--ink); }
  .person-name { font-size: 20px; line-height: 1.3; white-space: nowrap; }
  .person-role { font-size: 13px; color: var(--ink-soft); margin-top: 2px; }
  .contact-list { position: absolute; list-style: none; font-size: 14px; color: var(--ink); }
  .contact-list li { display: flex; align-items: center; gap: 8px; height: 22px; white-space: nowrap; }
  .contact-list svg { width: 13px; height: 13px; fill: var(--ink); flex: none; }
  .phones { left: 130px; top: 200px; }
  .web { left: 300px; top: 156px; }
  .address-band {
    position: absolute; left: 0; right: 0; bottom: 0; height: 50px;
    background: var(--green);
    color: var(--green-pale);
    font-size: 15px;
    display: flex; align-items: center;
    padding-left: 130px;
    white-space: nowrap;
  }
</style>
</head>
<body>
  <section class="card card-back">
    <div class="side-band"></div>
    <div class="brand-name">Varuko</div>
  </section>

  <section class="card card-front">
    <div class="brand">
      <span class="brand-dot"></span>
      <span class="brand-word">Varuko</span>
    </div>

    <div class="person">
      <div class="person-name">Daniel Morrow</div>
      <div class="person-role">managing director</div>
    </div>

    <ul class="contact-list web">
      <li><svg viewBox="0 0 16 16"><path d="M1 3h14v10H1z M1 3l7 6 7-6" fill="none" stroke="#4f5a63" stroke-width="1.6"/></svg>dmorrow@varukogroup.com</li>
      <li><svg viewBox="0 0 16 16"><circle cx="8" cy="8" r="6.5" fill="none" stroke="#4f5a63" stroke-width="1.5"/><path d="M1.5 8h13M8 1.5c-3 3.5-3 9.5 0 13M8 1.5c3 3.5 3 9.5 0 13" fill="none" stroke="#4f5a63" stroke-width="1.2"/></svg>www.varukogroup.com</li>
    </ul>

    <ul class="contact-list phones">
      <li><svg viewBox="0 0 16 16"><path d="M4 1.5l2.5 3-1.5 2c1 2 2.5 3.5 4.5 4.5l2-1.5 3 2.5-1.5 2.5C7.5 14.5 1.5 8.5 1.5 3z"/></svg>646 203 41 87</li>
      <li><svg viewBox="0 0 16 16"><rect x="4" y="1" width="8" height="14" rx="1.5" fill="none" stroke="#4f5a63" stroke-width="1.6"/><circle cx="8" cy="12.5" r="1"/></svg>917 482 30 65</li>
    </ul>

    <div class="address-band">48 Ridge Lane, Hillvale, New York 10458</div>
  </section>
</body>
</html>
```